Product Introduction Brochure

Brochure to introduce our mid/high end lighting products to potential wholesalers / Disrtibutors / Retailers. To be mainly graphical but will contain some text also. The purpose of the brochure will be to get potential customers to find out more either by calling us or to visit our website. The brochure should be of A3 size folded in half to an A4. Front page should be mainly logo and name, inner 2 pages should showcase some of the products we can supply together with some text (to be supplied, please use filler text in the initial design), then the back page containing our contact details. The products are lights, floor lamps and table lamps. I have attached a number of images, as well as our company logo. I would prefer the design to be on a black background, however this is not critical
Target Market(s)
Retailer, distribution and wholesale buyers
Interior design consultants and specifiers
Industry/Entity Type
Product
Look and feel
Each slider illustrates characteristics of the customer's brand and the style your logo design should communicate.

```html
<!DOCTYPE html>
<html lang="en">
<head>
<meta charset="UTF-8">
<title>Lumora — Product Introduction Brochure Cover</title>
<link rel="stylesheet" href="https://fonts.googleapis.com/css2?family=Roboto:wght@700&display=swap">
<style>
  :root {
    --backdrop: #c9cdd6;
    --cover-black: #161616;
    --pattern-light: #e9e9e9;
    --pattern-dark: #2a2a2a;
    --brand-green: #2f9a3c;
  }
  html, body {
    margin: 0;
    padding: 0;
    width: 1200px;
    height: 797px;
    overflow: hidden;
    background: var(--backdrop);
  }
  .canvas {
    position: relative;
    width: 1200px;
    height: 797px;
  }
  .cover {
    position: absolute;
    left: 323px;
    top: 42px;
    width: 495px;
    height: 701px;
    background: var(--cover-black);
    overflow: hidden;
  }
  .cover-pattern {
    position: absolute;
    left: 0;
    top: 0;
    width: 495px;
    height: 420px;
    display: block;
  }
  .brand {
    position: absolute;
    left: 160px;
    top: 599px;
    display: flex;
    align-items: center;
    gap: 10px;
  }
  .brand-dot {
    width: 40px;
    height: 40px;
    border-radius: 50%;
    background: var(--brand-green);
  }
  .brand-name {
    font-family: "Roboto", Arial, sans-serif;
    font-weight: 700;
    font-size: 36px;
    line-height: 1;
    color: var(--brand-green);
    letter-spacing: 0.5px;
  }
</style>
</head>
<body>
  <main class="canvas">
    <section class="cover">
      <svg class="cover-pattern" viewBox="0 0 495 420" role="img"
           aria-label="Large black-and-white diamond checker pattern inside a circular shape">
        <defs>
          <linearGradient id="patternTone" x1="0" y1="0" x2="1" y2="1">
            <stop offset="0" stop-color="var(--pattern-light)"/>
            <stop offset="1" stop-color="var(--pattern-dark)"/>
          </linearGradient>
        </defs>
        <circle cx="247" cy="78" r="330" fill="url(#patternTone)"/>
      </svg>
      <div class="brand">
        <span class="brand-dot"></span>
        <span class="brand-name">Lumora</span>
      </div>
    </section>
  </main>
</body>
</html>
```